Banner 34"x81"

This is for a Pull Up Banner
I am supplying a sample of my logo and some of my art work for you to incorporate into an upright banner.
Please business name:LuellaRo OpenHarbor Psychotherapy
phone number: 583-214-9067 NOT THE ONE ON THE BUSINESS CARD

```html
<!DOCTYPE html>
<html lang="en">
<head>
<meta charset="utf-8">
<title>LuellaRo OpenHarbor Psychotherapy – Pull Up Banner</title>
<link rel="stylesheet" href="https://fonts.googleapis.com/css2?family=Josefin+Sans:wght@300&family=Oswald:wght@600;700&display=swap">
<style>
  :root {
    --page-bg: #ffffff;
    --banner-navy: #1b222b;
    --photo-blue: #4a75c0;
    --photo-blue-deep: #2f58a3;
    --photo-blue-light: #8fb0e4;
    --divider-white: #ffffff;
    --title-grey: #e4e6ea;
    --text-white: #ffffff;
    --accent-red: #e0141c;
  }
  html, body {
    margin: 0;
    padding: 0;
    width: 1030px;
    height: 1200px;
    overflow: hidden;
    background: var(--page-bg);
  }
  .canvas {
    position: relative;
    width: 1030px;
    height: 1200px;
  }
  .banner {
    position: absolute;
    left: 280px;
    top: 39px;
    width: 471px;
    height: 1122px;
    display: block;
  }
  .vertical-title {
    font-family: "Oswald", sans-serif;
    font-weight: 700;
    fill: var(--title-grey);
  }
  .practice-name {
    font-family: "Oswald", sans-serif;
    font-weight: 600;
    fill: var(--text-white);
  }
  .practice-tagline,
  .phone-number {
    font-family: "Josefin Sans", sans-serif;
    font-weight: 300;
    fill: var(--text-white);
  }
</style>
</head>
<body>
<main class="canvas">
  <svg class="banner" viewBox="0 0 453 1079" xmlns="http://www.w3.org/2000/svg">
    <defs>
      <linearGradient id="portraitBase" x1="0" y1="0" x2="1" y2="1">
        <stop offset="0" stop-color="var(--photo-blue-deep)"/>
        <stop offset="1" stop-color="var(--photo-blue)"/>
      </linearGradient>
      <radialGradient id="portraitGlow" cx="0.42" cy="0.5" r="0.45">
        <stop offset="0" stop-color="var(--photo-blue-light)" stop-opacity="0.85"/>
        <stop offset="1" stop-color="var(--photo-blue-light)" stop-opacity="0"/>
      </radialGradient>
    </defs>

    <!-- portrait area -->
    <g class="portrait" role="img" aria-label="Blue-toned portrait photo of the therapist smiling, seated on a tufted sofa">
      <rect x="0" y="0" width="453" height="500" fill="url(#portraitBase)"/>
      <rect x="0" y="0" width="453" height="500" fill="url(#portraitGlow)"/>
    </g>

    <!-- chevron divider -->
    <polygon class="divider-white" points="0,492 225,424 453,481 453,492 225,441" fill="var(--divider-white)"/>
    <polygon class="info-panel" points="0,492 225,441 453,492 453,1079 0,1079" fill="var(--banner-navy)"/>

    <!-- vertical service title -->
    <text class="vertical-title" transform="translate(425,801) rotate(-90)" x="0" y="0"
          font-size="104" textLength="747" lengthAdjust="spacing">PSYCHOTHERAPY</text>

    <!-- practice mark: plain square with name -->
    <rect class="name-square" x="108" y="548" width="116" height="116"
          fill="none" stroke="var(--text-white)" stroke-width="4"/>
    <text class="practice-name" x="166" y="740" font-size="54" text-anchor="middle"
          textLength="226" lengthAdjust="spacingAndGlyphs">LuellaRo</text>

    <text class="practice-tagline" x="233" y="870" font-size="62" text-anchor="middle"
          textLength="330" lengthAdjust="spacing">OpenHarbor</text>

    <!-- phone icon -->
    <g class="phone-icon" transform="translate(238,930)">
      <circle r="27" fill="none" stroke="var(--accent-red)" stroke-width="2.2"/>
      <path d="M-9,-11 L-5,-13 L-1,-6 L-4,-3 C-2,2 2,5 5,6 L8,3 L14,7 L12,11 C10,14 5,14 0,10 C-6,6 -11,0 -12,-5 C-12,-8 -11,-10 -9,-11 Z"
            fill="none" stroke="var(--accent-red)" stroke-width="1.8" stroke-linejoin="round"/>
    </g>

    <text class="phone-number" x="235" y="1035" font-size="70" text-anchor="middle"
          textLength="378" lengthAdjust="spacing">583-214-9067</text>
  </svg>
</main>
</body>
</html>
```